Popup Banners - BrightCounsel - Legal Technology

- We need two banners (same style) designed with two different images and different text.

- The details of the printing requirements are attached, along with suggested images.

- The banners should share the same theme as our website www.brightcounsel.com.au

- The first banner would include our logo (attached), use the 'roads join' image (attached) in some way and text: New Opportunities - Where legal services and technology meet.

- The second banner would include our logo (attached), use the 'jigsaw' image (attached) in some way and use text: Legal Technology Strategy, Advice and Capability.

- Details on what are required from the Printer is attached also.

Target Market(s)

Legal Professionals

Industry/Entity Type

Information Technology

Font styles to use
Sans Serif

Requirements
Must have
• Our logo (attached), suggested text and the image mentioned for each.
Nice to have
• Professional and modern look
Should not have
• Cheap looking

```html
<!DOCTYPE html>
<html lang="en">
<head>
<meta charset="utf-8">
<title>BrightCounsel Popup Banners</title>
<link rel="stylesheet" href="https://fonts.googleapis.com/css2?family=Arimo:wght@400;700&family=Lato:wght@400;700&display=swap">
<style>
  :root {
    --ink: #111111;
    --muted: #6f6f6f;
    --band-grey: #ececec;
    --sky-top: #b4f1fb;
    --sky-fade: #ffffff;
    --field-green: #4f8a2c;
    --field-sky: #2f6fb6;
    --night-blue: #0b1f45;
    --glow-blue: #3d8fd8;
    --icon-tone: #9aa7b4;
    --deco-grey: #efedec;
    --deco-blue: #f1fbfd;
    --white: #ffffff;
  }
  * { margin: 0; padding: 0; box-sizing: border-box; }
  html, body { width: 1029px; height: 1200px; overflow: hidden; background: var(--white); }
  .sheet { position: relative; width: 1029px; height: 1200px; }
  .banner {
    position: absolute; top: 0; width: 486px; height: 1200px;
    background: var(--white); overflow: hidden;
    font-family: "Lato", sans-serif; color: var(--ink);
  }
  .banner--roads { left: 0; }
  .banner--jigsaw { left: 542px; }

  .deco { position: absolute; z-index: 0; }
  .deco--top-grey { left: 250px; top: 20px; width: 120px; height: 120px; background: var(--deco-grey); }
  .deco--top-blue { left: 400px; top: 70px; width: 86px; height: 90px; background: var(--deco-blue); }
  .deco--low-grey { left: 148px; top: 830px; width: 170px; height: 230px; background: var(--deco-grey); opacity: .8; }
  .deco--low-blue { left: 262px; top: 830px; width: 224px; height: 280px; background: var(--deco-blue); }
  .deco--edge-grey { left: 0; top: 920px; width: 70px; height: 245px; background: var(--deco-grey); opacity: .7; }

  .brand-band, .hero, .follow, .office, .site-url { z-index: 1; }

  .brand-band {
    position: absolute; top: 147px; left: 0; width: 100%; height: 46px;
    background: var(--band-grey);
    display: flex; align-items: center; padding-left: 34px; gap: 12px;
  }
  .brand-mark { width: 18px; height: 18px; background: var(--ink); }
  .brand-name {
    font-family: "Arimo", sans-serif; font-size: 22px; letter-spacing: 6px; color: var(--ink);
  }

  .hero { position: absolute; top: 211px; left: 0; width: 100%; height: 325px; }
  .hero--roads { background: linear-gradient(180deg, var(--field-sky) 0%, #6fa3d6 18%, #7aa652 26%, var(--field-green) 60%, #3d6f22 100%); }
  .hero--jigsaw { background: radial-gradient(ellipse at 58% 42%, #dff3ff 0%, var(--glow-blue) 22%, #163a78 50%, var(--night-blue) 100%); }
  .hero-text {
    position: absolute; font-family: "Arimo", sans-serif; color: var(--white); text-align: center;
  }
  .hero-title { top: 22px; left: 0; width: 100%; font-size: 27px; }
  .hero-sub { top: 125px; left: 0; width: 100%; font-size: 23px; line-height: 28px; }
  .hero-caption {
    right: 20px; bottom: 14px; text-align: center; font-size: 14.5px; font-weight: 700; line-height: 18px;
  }

  .follow {
    position: absolute; top: 570px; left: 51px; height: 38px;
    display: flex; align-items: center;
  }
  .follow-label { font-size: 21px; color: var(--muted); width: 176px; }
  .follow-icon { width: 34px; height: 34px; background: var(--icon-tone); border-radius: 4px; margin-right: 55px; }

  .office {
    position: absolute; top: 638px; left: 0; width: 100%; height: 166px;
    background: linear-gradient(180deg, var(--sky-top) 0%, var(--sky-fade) 100%);
    text-align: center;
  }
  .office-title { margin-top: 47px; font-size: 22px; font-weight: 700; }
  .office-address { margin-top: 8px; font-size: 18px; }
  .office-phone { margin-top: 8px; font-size: 18px; display: flex; justify-content: center; align-items: center; gap: 8px; }

  .site-url {
    position: absolute; top: 1131px; right: 33px;
    font-family: "Arimo", sans-serif; font-size: 17px; letter-spacing: 2px;
  }
</style>
</head>
<body>
<div class="sheet">

  <section class="banner banner--roads">
    <span class="deco deco--top-grey"></span><span class="deco deco--top-blue"></span>
    <span class="deco deco--low-blue"></span><span class="deco deco--low-grey"></span><span class="deco deco--edge-grey"></span>
    <div class="brand-band"><span class="brand-mark"></span><span class="brand-name">BrightCounsel</span></div>
    <div class="hero hero--roads" role="img" aria-label="Photograph of two dirt roads joining across a green grassy hill under a blue sky">
      <p class="hero-text hero-title">NEW OPPORTUNITIES</p>
      <p class="hero-text hero-sub">-<br>WHERE<br>LEGAL SERVICES<br>AND TECHNOLOGY MEET</p>
    </div>
    <div class="follow">
      <span class="follow-label">Follow Us On :</span>
      <span class="follow-icon"></span><span class="follow-icon"></span><span class="follow-icon"></span>
    </div>
    <div class="office">
      <p class="office-title">Brisbane Office</p>
      <p class="office-address">Level 12, 48 Harbour Lane, Brisbane QLD 4000</p>
      <p class="office-phone">
        <svg width="22" height="22" viewBox="0 0 24 24" aria-hidden="true"><circle cx="12" cy="12" r="10.5" fill="none" stroke="#111" stroke-width="1.8"/><path d="M8.5 6.5l2 2.6-1.2 1.4c.8 1.8 2.2 3.2 4 4l1.4-1.2 2.6 2-1.4 2c-4.4-.4-8.4-4.4-8.8-8.8z" fill="#111"/></svg>
        07 3000 0142
      </p>
    </div>
    <p class="site-url">www.brightcounsel.com.au</p>
  </section>

  <section class="banner banner--jigsaw">
    <span class="deco deco--top-grey"></span><span class="deco deco--top-blue"></span>
    <span class="deco deco--low-blue"></span><span class="deco deco--low-grey"></span><span class="deco deco--edge-grey"></span>
    <div class="brand-band"><span class="brand-mark"></span><span class="brand-name">BrightCounsel</span></div>
    <div class="hero hero--jigsaw" role="img" aria-label="Photograph of a hand placing a glowing jigsaw piece into a dark blue puzzle">
      <p class="hero-text hero-caption">LEGAL TECHNOLOGY STRATEGY,<br>ADVICE AND CAPABILITY</p>
    </div>
    <div class="follow">
      <span class="follow-label">Follow Us On :</span>
      <span class="follow-icon"></span><span class="follow-icon"></span><span class="follow-icon"></span>
    </div>
    <div class="office">
      <p class="office-title">Brisbane Office</p>
      <p class="office-address">Level 12, 48 Harbour Lane, Brisbane QLD 4000</p>
      <p class="office-phone">
        <svg width="22" height="22" viewBox="0 0 24 24" aria-hidden="true"><circle cx="12" cy="12" r="10.5" fill="none" stroke="#111" stroke-width="1.8"/><path d="M8.5 6.5l2 2.6-1.2 1.4c.8 1.8 2.2 3.2 4 4l1.4-1.2 2.6 2-1.4 2c-4.4-.4-8.4-4.4-8.8-8.8z" fill="#111"/></svg>
        07 3000 0142
      </p>
    </div>
    <p class="site-url">www.brightcounsel.com.au</p>
  </section>

</div>
</body>
</html>
```